We need a cover designed for our book on parenting. The focus of this book is on the parents, not on the child! We like the idea of this title having a double meaning - insight as in gaining insights into parenting, and "in sight" as in looking inward as parents and how to improve ourselves rather than looking outward to improve our children. We would love for the cover to somehow represent this double meaning. I can upload an excerpt from the book soon over the next few days.
Updates

Reason: We are still reviewing the amazing designs! Thank you so much! :)

Target Market(s)

Parents with kids of any age from babies through adult children.

Requirements
Must have
• Title is: Steady Hearth Homes
• Subtitle is: Building Calm Households Daily
• Authors names: Tara Bellwin, LCSW Dorian Bellwin, Ph.D.

```html
<!DOCTYPE html>
<html lang="en">
<head>
<meta charset="utf-8">
<title>Steady Hearth Homes — Book Cover</title>
<link rel="stylesheet" href="https://fonts.googleapis.com/css2?family=Courgette&family=Open+Sans:wght@400;500&display=swap">
<style>
  :root {
    --cream: #f6ebdc;
    --ink: #5f5454;
    --ink-shadow: rgba(40, 30, 30, 0.4);
    --orange: #e89a1a;
    --blue: #2f76a0;
    --green: #2aa478;
    --red: #e8400f;
    --page: #ffffff;
  }
  * { margin: 0; padding: 0; box-sizing: border-box; }
  html, body {
    width: 960px;
    height: 1200px;
    overflow: hidden;
    background: var(--page);
  }
  .cover {
    position: relative;
    width: 960px;
    height: 1200px;
    background: var(--cream);
    border: 10px solid transparent;
    border-image: linear-gradient(100deg, var(--orange), var(--blue) 35%, var(--green) 65%, var(--red)) 1;
  }
  .cover-title {
    position: absolute;
    top: 120px;
    left: 0;
    width: 100%;
    text-align: center;
    color: var(--ink);
    font-weight: normal;
  }
  .title-script {
    display: block;
    font-family: "Courgette", cursive;
    font-size: 108px;
    line-height: 1.1;
    text-shadow: 2px 3px 2px var(--ink-shadow);
  }
  .title-caps {
    display: block;
    margin-top: 14px;
    font-family: "Open Sans", sans-serif;
    font-weight: 500;
    font-size: 100px;
    letter-spacing: 2px;
    line-height: 1;
    text-shadow: 2px 3px 2px var(--ink-shadow);
  }
  .cover-subtitle {
    position: absolute;
    top: 430px;
    left: 0;
    width: 100%;
    text-align: center;
    font-family: "Open Sans", sans-serif;
    font-weight: 400;
    font-size: 32px;
    letter-spacing: 1px;
    color: var(--ink);
  }
  .family-figures {
    position: absolute;
    left: 110px;
    top: 560px;
    width: 720px;
    height: 480px;
    background:
      linear-gradient(90deg,
        var(--orange) 0 18%, transparent 18% 30%,
        var(--blue) 30% 44%, transparent 44% 54%,
        var(--green) 54% 70%, transparent 70% 82%,
        var(--red) 82% 100%);
    opacity: 0.55;
    -webkit-mask-image: linear-gradient(180deg, #000 55%, rgba(0,0,0,0.3));
            mask-image: linear-gradient(180deg, #000 55%, rgba(0,0,0,0.3));
    border-radius: 12px;
  }
  .cover-authors {
    position: absolute;
    top: 1082px;
    left: 0;
    width: 100%;
    text-align: center;
    font-family: "Open Sans", sans-serif;
    font-weight: 500;
    font-size: 30px;
    line-height: 1.4;
    color: var(--ink);
  }
  .author { display: inline-block; margin: 0 22px; }
</style>
</head>
<body>
  <main class="cover">
    <h1 class="cover-title">
      <span class="title-script">Steady Hearth</span>
      <span class="title-caps">HOMES</span>
    </h1>
    <p class="cover-subtitle">Building Calm Households Daily</p>
    <div class="family-figures" role="img" aria-label="Four standing family figures in orange, blue, green and red, casting long soft shadows toward the viewer"></div>
    <p class="cover-authors">
      <span class="author">Tara Bellwin, LCSW</span>
      <span class="author">Dorian Bellwin, Ph.D.</span>
    </p>
  </main>
</body>
</html>
```